Professional Services Business Card Design

We need a business card design for a relatively new (less than one year old) company. Harrowmere Advisory Partners, LLC provides professional support services and expert assistance in acquisition management to federal agencies, and also provides acquisition workforce personnel training and development for defense and civilian agencies. The colors used should incorporate the colors found within the company's logo, which is attached.

Font styles to use
Serif
Sans Serif

```html
<!DOCTYPE html>
<html lang="en">
<head>
<meta charset="utf-8">
<title>Harrowmere Advisory Partners — Business Card Design</title>
<link rel="stylesheet" href="https://fonts.googleapis.com/css2?family=Tinos:wght@400;700&family=Open+Sans:wght@400&display=swap">
<style>
:root{
  --navy:#2c3358;
  --navy-deep:#262c4f;
  --lavender:#d4d9ea;
  --paper:#f4f5f9;
  --sheet:#eeeff2;
  --slate:#7e8291;
  --charcoal:#2f2f32;
  --ink:#3a3a3e;
  --white:#ffffff;
}
*{box-sizing:border-box;margin:0;padding:0}
html,body{width:1200px;height:3464px;overflow:hidden}
body{position:relative;background:var(--sheet);font-family:"Tinos",serif;color:var(--navy)}
.backdrop{position:absolute;inset:0;width:1200px;height:3464px}

.headline{position:absolute;left:69px;top:92px;font-size:62px;line-height:82px;font-weight:400;color:var(--navy);letter-spacing:1px}
.spec-list{position:absolute;left:82px;top:296px;list-style:none}
.spec-list li{position:relative;height:72px;padding-left:54px;font-size:34px;line-height:52px;color:var(--navy)}
.spec-list li::before{content:"";position:absolute;left:0;top:12px;width:30px;height:30px;background:var(--navy)}

.feature{position:absolute;top:962px;width:230px;margin-left:-115px;text-align:center;color:var(--white);font-family:"Open Sans",sans-serif;font-size:24px;line-height:32px}
.feature svg{display:block;margin:0 auto 16px;width:84px;height:88px}

.tagline{position:absolute;left:599px;top:2603px;transform:translate(-50%,-50%) rotate(-17.4deg);white-space:nowrap;font-size:36px;letter-spacing:1px;color:var(--ink)}
.tagline .divider{display:inline-block;width:2px;height:36px;background:var(--ink);margin:0 22px;vertical-align:-4px}

.card{position:absolute;width:894px;height:511px;overflow:hidden;transform-origin:0 0;box-shadow:16px 20px 26px rgba(0,0,0,.38)}
.card .shapes{position:absolute;inset:0;width:894px;height:511px}
.card-front{background:var(--paper)}
.card-back{background:var(--navy-deep)}

.name-bar{position:absolute;left:32px;top:109px;width:7px;height:80px;background:var(--navy)}
.holder-name{position:absolute;left:52px;top:104px;font-size:33px;line-height:40px;color:var(--navy)}
.holder-name b{font-weight:700}
.holder-title{position:absolute;left:52px;top:146px;font-size:26px;line-height:32px;color:var(--navy)}
.title-rule{position:absolute;left:52px;top:189px;width:372px;height:3px;background:var(--navy)}
.contact-list{position:absolute;left:34px;top:200px;list-style:none}
.contact-list li{position:relative;padding-left:38px;font-size:25px;line-height:32px;margin-bottom:17px;color:var(--navy)}
.contact-list svg{position:absolute;left:0;top:7px;width:20px;height:20px}

.wordmark{position:absolute;text-align:center;font-weight:400;text-transform:uppercase;letter-spacing:1px}
.wordmark .mark-square{display:block;margin:0 auto}
.wordmark .w-main{display:block}
.wordmark .w-sub{display:block}
.wordmark .w-llc{display:block;letter-spacing:3px}
.card-front .wordmark{left:420px;top:150px;width:474px;color:var(--navy)}
.card-front .mark-square{width:62px;height:62px;background:var(--navy);margin-bottom:46px}
.card-front .w-main{font-size:52px;line-height:56px}
.card-front .w-sub{font-size:31px;line-height:36px}
.card-front .w-llc{font-size:17px;line-height:24px}
.card-back .wordmark{left:300px;top:118px;width:560px;color:var(--white)}
.card-back .mark-square{width:78px;height:78px;background:var(--white);margin-bottom:52px}
.card-back .w-main{font-size:64px;line-height:68px}
.card-back .w-sub{font-size:38px;line-height:44px}
.card-back .w-llc{font-size:20px;line-height:28px}
</style>
</head>
<body>

<svg class="backdrop" viewBox="0 0 1200 3464" aria-hidden="true">
  <rect width="1200" height="3464" fill="var(--sheet)"/>
  <polygon points="0,742 1200,346 1200,1386 0,2053" fill="var(--slate)"/>
  <polygon points="0,2697 1200,2449 1200,3464 0,3464" fill="var(--charcoal)"/>
</svg>

<h1 class="headline">BUSINESS<br>CARD DESIGN</h1>
<ul class="spec-list">
  <li>3.5 X 2 INCHES</li>
  <li>ADOBE ILLUSTRATION</li>
  <li>FULLY EDITABLE</li>
  <li>PRINT READY</li>
  <li>300 DPI</li>
</ul>

<!-- feature icons -->
<div class="feature" style="left:136px">
  <svg viewBox="0 0 84 88" fill="none" stroke="#fff" stroke-width="4" stroke-linejoin="round"><path d="M10 4h40l16 16v64H10z"/><path d="M50 4v16h16"/><path d="M20 34h30M20 46h30M20 58h22M20 70h16"/><path d="M60 78l18-30 5 3-18 30-7 3z"/></svg>
  3.5 X 2 INCHES<br>WITH BLEED
</div>
<div class="feature" style="left:366px">
  <svg viewBox="0 0 84 88" fill="none" stroke="#fff" stroke-width="4" stroke-linejoin="round"><path d="M22 30V8h40v22"/><rect x="6" y="30" width="72" height="34" rx="6"/><path d="M22 52h40v30H22z"/><path d="M30 62h24M30 72h24"/><circle cx="66" cy="40" r="2.5" fill="#fff"/></svg>
  PRINT<br>READY
</div>
<div class="feature" style="left:594px">
  <svg viewBox="0 0 84 88" fill="none" stroke="#fff" stroke-width="4" stroke-linejoin="round"><path d="M16 14h42v66H16z"/><path d="M28 14V6h42v64h-12"/></svg>
  FULLY<br>EDITABLE
</div>
<div class="feature" style="left:816px">
  <svg viewBox="0 0 84 88" fill="none" stroke="#fff" stroke-width="4" stroke-linejoin="round"><rect x="6" y="10" width="72" height="20" rx="3"/><rect x="6" y="36" width="72" height="20" rx="3"/><rect x="6" y="62" width="72" height="20" rx="3"/><path d="M26 10v20M26 36v20M26 62v20"/></svg>
  LAYER<br>&amp; ORGANIZED
</div>
<div class="feature" style="left:1039px">
  <svg viewBox="0 0 84 88" fill="none" stroke="#fff" stroke-width="4" stroke-linejoin="round"><path d="M30 6h24M34 6v28L10 76a6 6 0 0 0 5 8h54a6 6 0 0 0 5-8L50 34V6"/><path d="M20 58h44"/></svg>
  PROFESSIONAL<br>DESIGN
</div>

<div class="tagline">PROFESSIONAL DESIGN<span class="divider"></span>BUSINESS CARD</div>

<!-- Front card template repeated -->
<div class="card card-front" style="left:584px;top:99px;transform:scale(.614)">
  <svg class="shapes" viewBox="0 0 894 511" aria-hidden="true"><polygon points="495,0 894,0 894,511 379,511" fill="var(--lavender)"/><polygon points="317,0 495,0 460,154" fill="var(--navy)"/></svg>
  <div class="name-bar"></div>
  <p class="holder-name">Colton <b>Merrick</b></p>
  <p class="holder-title">Managing Director</p>
  <div class="title-rule"></div>
  <ul class="contact-list">
    <li><svg viewBox="0 0 20 20"><path fill="var(--navy)" d="M6 1h8a2 2 0 0 1 2 2v14a2 2 0 0 1-2 2H6a2 2 0 0 1-2-2V3a2 2 0 0 1 2-2zm0 3v11h8V4z"/></svg>0522 48 90317</li>
    <li><svg viewBox="0 0 20 20"><path fill="var(--navy)" d="M1 4h18v12H1zm2 2v1l7 5 7-5V6l-7 5z"/></svg>info@hap.com</li>
    <li><svg viewBox="0 0 20 20" fill="none" stroke="var(--navy)" stroke-width="2"><circle cx="10" cy="10" r="8"/><path d="M2 10h16M10 2c-4 5-4 11 0 16M10 2c4 5 4 11 0 16"/></svg>www.hap.com.au</li>
    <li><svg viewBox="0 0 20 20"><path fill="var(--navy)" d="M10 1a6 6 0 0 1 6 6c0 5-6 12-6 12S4 12 4 7a6 6 0 0 1 6-6zm0 4a2 2 0 1 0 0 4 2 2 0 0 0 0-4z"/></svg>2204/61 hollis lane,<br>brisbane qld 4000</li>
  </ul>
  <div class="wordmark"><span class="mark-square"></span><span class="w-main">Harrowmere</span><span class="w-sub">Advisory Partners</span><span class="w-llc">LLC</span></div>
</div>

<div class="card card-back" style="left:584px;top:482px;transform:scale(.614)">
  <svg class="shapes" viewBox="0 0 894 511" aria-hidden="true"><polygon points="195,0 212,0 32,511 15,511" fill="var(--lavender)"/><polygon points="232,0 345,0 165,511 52,511" fill="var(--lavender)"/></svg>
  <div class="wordmark"><span class="mark-square"></span><span class="w-main">Harrowmere</span><span class="w-sub">Advisory Partners</span><span class="w-llc">LLC</span></div>
</div>

<div class="card card-front" style="left:153px;top:1244px">
  <svg class="shapes" viewBox="0 0 894 511" aria-hidden="true"><polygon points="495,0 894,0 894,511 379,511" fill="var(--lavender)"/><polygon points="317,0 495,0 460,154" fill="var(--navy)"/></svg>
  <div class="name-bar"></div>
  <p class="holder-name">Colton <b>Merrick</b></p>
  <p class="holder-title">Managing Director</p>
  <div class="title-rule"></div>
  <ul class="contact-list">
    <li><svg viewBox="0 0 20 20"><path fill="var(--navy)" d="M6 1h8a2 2 0 0 1 2 2v14a2 2 0 0 1-2 2H6a2 2 0 0 1-2-2V3a2 2 0 0 1 2-2zm0 3v11h8V4z"/></svg>0522 48 90317</li>
    <li><svg viewBox="0 0 20 20"><path fill="var(--navy)" d="M1 4h18v12H1zm2 2v1l7 5 7-5V6l-7 5z"/></svg>info@hap.com</li>
    <li><svg viewBox="0 0 20 20" fill="none" stroke="var(--navy)" stroke-width="2"><circle cx="10" cy="10" r="8"/><path d="M2 10h16M10 2c-4 5-4 11 0 16M10 2c4 5 4 11 0 16"/></svg>www.hap.com.au</li>
    <li><svg viewBox="0 0 20 20"><path fill="var(--navy)" d="M10 1a6 6 0 0 1 6 6c0 5-6 12-6 12S4 12 4 7a6 6 0 0 1 6-6zm0 4a2 2 0 1 0 0 4 2 2 0 0 0 0-4z"/></svg>2204/61 hollis lane,<br>brisbane qld 4000</li>
  </ul>
  <div class="wordmark"><span class="mark-square"></span><span class="w-main">Harrowmere</span><span class="w-sub">Advisory Partners</span><span class="w-llc">LLC</span></div>
</div>

<div class="card card-back" style="left:156px;top:1868px;transform:scale(.977)">
  <svg class="shapes" viewBox="0 0 894 511" aria-hidden="true"><polygon points="195,0 212,0 32,511 15,511" fill="var(--lavender)"/><polygon points="232,0 345,0 165,511 52,511" fill="var(--lavender)"/></svg>
  <div class="wordmark"><span class="mark-square"></span><span class="w-main">Harrowmere</span><span class="w-sub">Advisory Partners</span><span class="w-llc">LLC</span></div>
</div>

<!-- presentation grid -->
<div class="card card-back" style="left:74px;top:2815px;transform:scale(.346)">
  <svg class="shapes" viewBox="0 0 894 511" aria-hidden="true"><polygon points="195,0 212,0 32,511 15,511" fill="var(--lavender)"/><polygon points="232,0 345,0 165,511 52,511" fill="var(--lavender)"/></svg>
  <div class="wordmark"><span class="mark-square"></span><span class="w-main">Harrowmere</span><span class="w-sub">Advisory Partners</span><span class="w-llc">LLC</span></div>
</div>

<div class="card card-front" style="left:403px;top:2766px;transform:scale(.449)">
  <svg class="shapes" viewBox="0 0 894 511" aria-hidden="true"><polygon points="495,0 894,0 894,511 379,511" fill="var(--lavender)"/><polygon points="317,0 495,0 460,154" fill="var(--navy)"/></svg>
  <div class="name-bar"></div>
  <p class="holder-name">Colton <b>Merrick</b></p>
  <p class="holder-title">Managing Director</p>
  <div class="title-rule"></div>
  <ul class="contact-list">
    <li><svg viewBox="0 0 20 20"><path fill="var(--navy)" d="M6 1h8a2 2 0 0 1 2 2v14a2 2 0 0 1-2 2H6a2 2 0 0 1-2-2V3a2 2 0 0 1 2-2zm0 3v11h8V4z"/></svg>0522 48 90317</li>
    <li><svg viewBox="0 0 20 20"><path fill="var(--navy)" d="M1 4h18v12H1zm2 2v1l7 5 7-5V6l-7 5z"/></svg>info@hap.com</li>
    <li><svg viewBox="0 0 20 20" fill="none" stroke="var(--navy)" stroke-width="2"><circle cx="10" cy="10" r="8"/><path d="M2 10h16M10 2c-4 5-4 11 0 16M10 2c4 5 4 11 0 16"/></svg>www.hap.com.au</li>
    <li><svg viewBox="0 0 20 20"><path fill="var(--navy)" d="M10 1a6 6 0 0 1 6 6c0 5-6 12-6 12S4 12 4 7a6 6 0 0 1 6-6zm0 4a2 2 0 1 0 0 4 2 2 0 0 0 0-4z"/></svg>2204/61 hollis lane,<br>brisbane qld 4000</li>
  </ul>
  <div class="wordmark"><span class="mark-square"></span><span class="w-main">Harrowmere</span><span class="w-sub">Advisory Partners</span><span class="w-llc">LLC</span></div>
</div>

<div class="card card-back" style="left:816px;top:2815px;transform:scale(.346)">
  <svg class="shapes" viewBox="0 0 894 511" aria-hidden="true"><polygon points="195,0 212,0 32,511 15,511" fill="var(--lavender)"/><polygon points="232,0 345,0 165,511 52,511" fill="var(--lavender)"/></svg>
  <div class="wordmark"><span class="mark-square"></span><span class="w-main">Harrowmere</span><span class="w-sub">Advisory Partners</span><span class="w-llc">LLC</span></div>
</div>

<div class="card card-front" style="left:74px;top:3031px;transform:scale(.346)">
  <svg class="shapes" viewBox="0 0 894 511" aria-hidden="true"><polygon points="495,0 894,0 894,511 379,511" fill="var(--lavender)"/><polygon points="317,0 495,0 460,154" fill="var(--navy)"/></svg>
  <div class="name-bar"></div>
  <p class="holder-name">Colton <b>Merrick</b></p>
  <p class="holder-title">Managing Director</p>
  <div class="title-rule"></div>
  <ul class="contact-list">
    <li><svg viewBox="0 0 20 20"><path fill="var(--navy)" d="M6 1h8a2 2 0 0 1 2 2v14a2 2 0 0 1-2 2H6a2 2 0 0 1-2-2V3a2 2 0 0 1 2-2zm0 3v11h8V4z"/></svg>0522 48 90317</li>
    <li><svg viewBox="0 0 20 20"><path fill="var(--navy)" d="M1 4h18v12H1zm2 2v1l7 5 7-5V6l-7 5z"/></svg>info@hap.com</li>
    <li><svg viewBox="0 0 20 20" fill="none" stroke="var(--navy)" stroke-width="2"><circle cx="10" cy="10" r="8"/><path d="M2 10h16M10 2c-4 5-4 11 0 16M10 2c4 5 4 11 0 16"/></svg>www.hap.com.au</li>
    <li><svg viewBox="0 0 20 20"><path fill="var(--navy)" d="M10 1a6 6 0 0 1 6 6c0 5-6 12-6 12S4 12 4 7a6 6 0 0 1 6-6zm0 4a2 2 0 1 0 0 4 2 2 0 0 0 0-4z"/></svg>2204/61 hollis lane,<br>brisbane qld 4000</li>
  </ul>
  <div class="wordmark"><span class="mark-square"></span><span class="w-main">Harrowmere</span><span class="w-sub">Advisory Partners</span><span class="w-llc">LLC</span></div>
</div>

<div class="card card-back" style="left:403px;top:3031px;transform:scale(.449)">
  <svg class="shapes" viewBox="0 0 894 511" aria-hidden="true"><polygon points="195,0 212,0 32,511 15,511" fill="var(--lavender)"/><polygon points="232,0 345,0 165,511 52,511" fill="var(--lavender)"/></svg>
  <div class="wordmark"><span class="mark-square"></span><span class="w-main">Harrowmere</span><span class="w-sub">Advisory Partners</span><span class="w-llc">LLC</span></div>
</div>

<div class="card card-front" style="left:816px;top:3031px;transform:scale(.346)">
  <svg class="shapes" viewBox="0 0 894 511" aria-hidden="true"><polygon points="495,0 894,0 894,511 379,511" fill="var(--lavender)"/><polygon points="317,0 495,0 460,154" fill="var(--navy)"/></svg>
  <div class="name-bar"></div>
  <p class="holder-name">Colton <b>Merrick</b></p>
  <p class="holder-title">Managing Director</p>
  <div class="title-rule"></div>
  <ul class="contact-list">
    <li><svg viewBox="0 0 20 20"><path fill="var(--navy)" d="M6 1h8a2 2 0 0 1 2 2v14a2 2 0 0 1-2 2H6a2 2 0 0 1-2-2V3a2 2 0 0 1 2-2zm0 3v11h8V4z"/></svg>0522 48 90317</li>
    <li><svg viewBox="0 0 20 20"><path fill="var(--navy)" d="M1 4h18v12H1zm2 2v1l7 5 7-5V6l-7 5z"/></svg>info@hap.com</li>
    <li><svg viewBox="0 0 20 20" fill="none" stroke="var(--navy)" stroke-width="2"><circle cx="10" cy="10" r="8"/><path d="M2 10h16M10 2c-4 5-4 11 0 16M10 2c4 5 4 11 0 16"/></svg>www.hap.com.au</li>
    <li><svg viewBox="0 0 20 20"><path fill="var(--navy)" d="M10 1a6 6 0 0 1 6 6c0 5-6 12-6 12S4 12 4 7a6 6 0 0 1 6-6zm0 4a2 2 0 1 0 0 4 2 2 0 0 0 0-4z"/></svg>2204/61 hollis lane,<br>brisbane qld 4000</li>
  </ul>
  <div class="wordmark"><span class="mark-square"></span><span class="w-main">Harrowmere</span><span class="w-sub">Advisory Partners</span><span class="w-llc">LLC</span></div>
</div>

</body>
</html>
```